Bramwell Resources Ltd. - Refreshed business card challenge

A revised, refreshed business card design for my oil and gas company using my existing logo. Feel free to be as creative as you like!

Target Market(s)

bankers, lawyers

Industry/Entity Type

Oil And Gas Exploration

Contact Information for Business Card

See the "Must Haves" section

Font styles to use
Serif
Sans Serif

Colors

Designer to choose colors to be used in the design.

Requirements
Must have
• Existing business logo, name, title, email, phone number, business address
• Neil Hadley, CA, CPA
• Vice President Finance & Chief Financial Officer
• nhadley@bramwellresources-mail.com
• office: (587)555-0142
• cell: (403)555-0187
• 1400, 815 4 Street S.W.
• Calgary, AB
• T2P 4K8
Should not have
• Should not be plain and boring.

```html
<!DOCTYPE html>
<html lang="en">
<head>
<meta charset="utf-8">
<title>Bramwell Resources – Business Card</title>
<link href="https://fonts.googleapis.com/css2?family=Exo+2:wght@500;600;700;800&display=swap" rel="stylesheet">
<style>
  :root {
    --page: #ece8e2;
    --gold: #d9981f;
    --maroon: #5b1f12;
    --umber: #4a2008;
    --night-brown: #250c02;
    --forest: #0d4a33;
    --paper-text: #ffffff;
  }
  * { margin: 0; padding: 0; box-sizing: border-box; }
  html, body {
    width: 1200px; height: 900px; overflow: hidden;
    background: var(--page);
    font-family: "Exo 2", "Segoe UI", sans-serif;
  }
  .sheet {
    position: relative; width: 1200px; height: 900px;
  }
  .card {
    position: absolute; left: 250px; width: 700px; height: 400px;
    overflow: hidden; border-radius: 4px;
    box-shadow: 0 6px 18px rgba(40, 20, 5, 0.22);
  }
  .card--info { top: 35px; background: var(--gold); }
  .card--brand { top: 465px; background: var(--gold); }
  .card__waves { position: absolute; inset: 0; width: 700px; height: 400px; }

  .info-panel {
    position: absolute; left: 0; top: 0; width: 390px; height: 400px;
    color: var(--paper-text);
    padding: 58px 0 0 46px;
  }
  .contact-name {
    font-size: 25px; font-weight: 700; letter-spacing: 4px;
    text-transform: uppercase;
  }
  .contact-name .credentials {
    font-size: 11px; font-weight: 500; letter-spacing: 2px; margin-left: 4px;
  }
  .contact-title { font-size: 14px; font-weight: 600; margin-top: 6px; }
  .contact-address { font-size: 14.5px; font-weight: 500; line-height: 1.2; margin-top: 26px; }
  .contact-phones { font-size: 15px; font-weight: 500; line-height: 1.2; margin-top: 22px; }
  .contact-email { font-size: 13px; font-weight: 600; margin-top: 24px; }

  .wordmark {
    position: absolute; color: var(--forest); font-weight: 800;
    line-height: 1; text-align: right;
  }
  .wordmark__name { display: block; }
  .wordmark__sub { display: block; letter-spacing: 2px; text-transform: uppercase; }
  .card--info .wordmark { left: 430px; top: 120px; width: 230px; }
  .card--info .wordmark__name { font-size: 46px; }
  .card--info .wordmark__sub { font-size: 13px; margin-top: 4px; }
  .card--brand .wordmark { left: 300px; top: 150px; width: 300px; }
  .card--brand .wordmark__name { font-size: 64px; }
  .card--brand .wordmark__sub { font-size: 17px; margin-top: 6px; }
</style>
</head>
<body>
<main class="sheet">

  <section class="card card--info" aria-label="Business card, contact side">
    <svg class="card__waves" viewBox="0 0 700 400" aria-hidden="true">
      <rect x="0" y="0" width="390" height="400" fill="var(--maroon)"/>
      <path d="M0,210 C60,300 170,360 270,355 C380,350 420,250 500,215 C580,180 650,210 700,250 L700,400 L0,400 Z" fill="var(--umber)"/>
      <path d="M0,226 C60,320 170,380 270,376 C380,372 425,275 505,240 C585,205 650,232 700,272 L700,400 L0,400 Z" fill="var(--night-brown)"/>
    </svg>
    <div class="info-panel">
      <h1 class="contact-name">Neil Hadley<span class="credentials">CA.CPA</span></h1>
      <p class="contact-title">Vice President Finance &amp; Chief Financial Officer</p>
      <p class="contact-address">1400, 815 4 Street S.W.<br>Calgary, AB<br>T2P 4K8</p>
      <p class="contact-phones">(587)555-0142<br>(403)555-0187</p>
      <p class="contact-email">nhadley@bramwellresources-mail.com</p>
    </div>
    <div class="wordmark">
      <span class="wordmark__name">Bramwell</span>
      <span class="wordmark__sub">Resources</span>
    </div>
  </section>

  <section class="card card--brand" aria-label="Business card, brand side">
    <svg class="card__waves" viewBox="0 0 700 400" aria-hidden="true">
      <path d="M0,345 C90,235 170,178 250,190 C340,205 400,315 480,355 C570,395 655,320 685,110 L700,20 L700,400 L0,400 Z" fill="var(--umber)"/>
      <path d="M0,362 C90,255 170,200 250,212 C340,226 400,336 480,376 C570,416 662,340 690,135 L700,60 L700,400 L0,400 Z" fill="var(--night-brown)"/>
    </svg>
    <div class="wordmark">
      <span class="wordmark__name">Bramwell</span>
      <span class="wordmark__sub">Resources</span>
    </div>
  </section>

</main>
</body>
</html>
```